Post Card Invitation to Wedding Rehearsal Dinner and After Party

This post card should serve as invitations for two events in the wedding weekend for two San Francisco grooms, Derek and Simon.
Each side of the card should have distinct looks and information but tied together with “Before” on the front and “After” on the back.
POST CARD FRONT
Required text:
BEFORE
Derek and Simon’s Wedding: Rehearsal Dinner
Friday, May 22, 2015
5:30 PM
Larkvale Grub Yard
617 Tessler Avenue @ Marlow
San Francisco, CA
Please also convey the following information without necessarily quoting directly: This rehearsal dinner will be held in a private enclosed space in the food truck park. We we will serve beer and wine in our space and provide tickets to purchase food from any of the trucks in the park. Dress is casual.
Look and feel of the card should have a modern, “hipster” feel to it. If you search Google images for “Hipster design” or “hipster infographic” you should get a sense of the overall design and colors. The website for the venue is http://larkvalegrubyard.com/ for reference but please DO NOT use any images or logos from the site.
----------------------
POST CARD REVERSE
Required Text:
AFTER
Derek and Simon’s Wedding: After Party
Saturday, May 23, 2015
7:30 PM
Corvell Harbor Sailing Club
42 Pennick Lane
San Francisco, CA
Please also convey the following information without necessarily quoting directly: Black-tie optional. Dancing, snacks and dessert and cocktails with panoramic views of the San Francisco Bay and Golden Gate Bridge.
This should have a much different look and feel from the front of the card. It should convey an elegant black-tie affair. If you search Google images for “black tie after party invitation” you should get some examples of an overall feel that I am aiming for. The website for the venue is www.chsclub.com but DO NOT use any of the images or logos from the site.
Industry/Entity Type
Wedding
Look and feel
Each slider illustrates characteristics of the customer's brand and the style your logo design should communicate.

```html
<!DOCTYPE html>
<html lang="en">
<head>
<meta charset="utf-8">
<title>Derek &amp; Simon – Rehearsal Dinner &amp; After Party</title>
<link rel="stylesheet" href="https://fonts.googleapis.com/css2?family=Bebas+Neue&family=Oswald:wght@400;500;600&family=Pacifico&family=Josefin+Sans:wght@300;400;600&display=swap">
<style>
  :root {
    --page-bg: #e9e6df;
    --kraft: #dcd0b4;
    --charcoal: #464340;
    --coral: #e6473c;
    --teal: #1d8584;
    --blush: #f4d8d2;
    --white: #ffffff;
    --ink: #0a0a0a;
    --accent-red: #d3231f;
    --silver: #d8d8d8;
  }
  * { box-sizing: border-box; margin: 0; padding: 0; }
  html, body { width: 1200px; height: 900px; overflow: hidden; }
  body { background: var(--page-bg); position: relative; }

  .card { position: absolute; top: 70px; width: 440px; height: 760px; overflow: hidden;
          box-shadow: 0 4px 18px rgba(0,0,0,.18); }

  /* ---------- Front: rehearsal dinner ---------- */
  .card--before { left: 110px; background: var(--kraft); color: var(--charcoal); }
  .before__band-top { position: absolute; top: 0; left: 0; right: 0; height: 58px; background: var(--charcoal); }
  .before__band-bottom { position: absolute; bottom: 0; left: 0; right: 0; height: 62px; background: var(--charcoal); }
  .before__tab { position: absolute; top: 10px; left: 50%; transform: translateX(-50%);
                 width: 210px; height: 78px; background: var(--kraft);
                 border: 6px solid var(--charcoal); border-bottom: none; border-radius: 80px 80px 0 0;
                 font-family: "Bebas Neue", sans-serif; font-size: 52px; line-height: 78px; text-align: center; }
  .before__bowtie { position: absolute; border-radius: 14px; }
  .before__bowtie--coral { left: 52px; top: 112px; width: 120px; height: 66px; background: var(--coral); }
  .before__bowtie--teal { left: 272px; top: 104px; width: 112px; height: 58px; background: var(--teal); }
  .before__names { position: absolute; top: 176px; left: 0; right: 0; display: flex; justify-content: center;
                   align-items: center; gap: 10px; font-family: "Bebas Neue", sans-serif; font-size: 92px;
                   font-weight: 400; line-height: 1; }
  .before__name--coral { color: var(--coral); }
  .before__name--teal { color: var(--teal); }
  .before__amp { width: 46px; height: 46px; border-radius: 50%; background: var(--blush); color: var(--coral);
                 font-family: "Oswald", sans-serif; font-size: 30px; line-height: 46px; text-align: center; }
  .before__ribbon { position: absolute; top: 290px; left: 28px; right: 28px; height: 60px; background: var(--charcoal);
                    display: flex; align-items: center; justify-content: space-between; padding: 0 16px; color: var(--kraft); }
  .before__ribbon-title { font-family: "Pacifico", cursive; font-size: 28px; line-height: 1; color: var(--kraft); }
  .before__star { font-size: 18px; }
  .before__dates { position: absolute; top: 374px; left: 0; right: 0; display: flex; justify-content: center; align-items: center; gap: 14px; }
  .date-box { width: 150px; text-align: center; font-family: "Oswald", sans-serif; }
  .date-box__top { background: var(--teal); color: var(--white); font-size: 36px; font-weight: 500; height: 54px; line-height: 54px; }
  .date-box__bottom { border: 4px solid var(--teal); border-top: none; color: var(--teal); font-size: 30px; height: 54px; line-height: 48px; }
  .chevrons { width: 34px; height: 24px; }
  .before__venue { position: absolute; top: 500px; left: 0; right: 0; text-align: center;
                   font-family: "Oswald", sans-serif; font-style: normal; white-space: nowrap; }
  .before__venue-name { font-size: 22px; }
  .before__venue-street { font-size: 19px; margin-top: 4px; }
  .before__details { position: absolute; top: 594px; left: 28px; right: 28px; display: flex; gap: 12px; height: 82px; }
  .detail-box { background: var(--coral); color: var(--white); display: flex; flex-direction: column;
                justify-content: center; align-items: center; text-align: center; }
  .detail-box--dress { width: 118px; font-family: "Oswald", sans-serif; font-size: 22px; line-height: 1.1; }
  .detail-box--dress span { display: block; border: 2px solid var(--white); padding: 6px 10px; }
  .detail-box--food { flex: 1; outline: 2px dashed rgba(255,255,255,.7); outline-offset: -6px; padding: 0 10px; }
  .detail-box__script { font-family: "Pacifico", cursive; font-size: 22px; line-height: 1.2; }
  .detail-box__note { font-family: "Oswald", sans-serif; font-size: 11px; margin-top: 4px; }

  /* ---------- Back: after party ---------- */
  .card--after { left: 650px; background: radial-gradient(ellipse at 50% 35%, #262626 0%, var(--ink) 70%); color: var(--white); }
  .after__frame { position: absolute; inset: 22px; border: 2px solid var(--white); }
  .after__label { position: absolute; top: 4px; left: 50%; transform: translateX(-50%); background: var(--ink);
                  padding: 0 14px; font-family: "Josefin Sans", sans-serif; font-size: 44px; letter-spacing: 2px; }
  .after__tuxedo { position: absolute; top: 66px; left: 70px; width: 300px; height: 320px;
                   border-radius: 40% 40% 20% 20%;
                   background: radial-gradient(ellipse at 50% 25%, #f2f2f2 0%, #bdbdbd 14%, #2e2e2e 32%, #121212 75%); }
  .after__names { position: absolute; top: 384px; left: 0; right: 0; text-align: center;
                  font-family: "Pacifico", cursive; font-size: 46px; font-weight: 400; }
  .after__title { position: absolute; top: 476px; left: 0; right: 0; text-align: center;
                  font-family: "Josefin Sans", sans-serif; font-size: 36px; letter-spacing: 3px; }
  .after__rule { position: absolute; left: 140px; right: 140px; height: 2px; background: var(--accent-red); }
  .after__rule--one { top: 526px; }
  .after__rule--two { top: 588px; }
  .after__rule--three { top: 688px; }
  .after__date { position: absolute; top: 542px; left: 0; right: 0; text-align: center;
                 font-family: "Josefin Sans", sans-serif; font-weight: 300; font-size: 24px; letter-spacing: 1px; color: var(--silver); }
  .after__where { position: absolute; top: 608px; left: 36px; right: 36px; text-align: center;
                  font-family: "Josefin Sans", sans-serif; font-style: normal; font-size: 17px;
                  line-height: 1.6; letter-spacing: .5px; white-space: nowrap; }
  .after__note { position: absolute; top: 698px; left: 40px; right: 40px; text-align: center;
                 font-family: "Josefin Sans", sans-serif; font-size: 10px; line-height: 1.4; color: var(--silver); }
</style>
</head>
<body>

<section class="card card--before" aria-label="Rehearsal dinner invitation">
  <div class="before__band-top"></div>
  <div class="before__tab">BEFORE</div>
  <div class="before__bowtie before__bowtie--coral" role="img" aria-label="Red polka-dot bow tie illustration"></div>
  <div class="before__bowtie before__bowtie--teal" role="img" aria-label="Teal striped bow tie illustration"></div>

  <h1 class="before__names">
    <span class="before__name--coral">DEREK</span>
    <span class="before__amp">&amp;</span>
    <span class="before__name--teal">SIMON</span>
  </h1>

  <div class="before__ribbon">
    <span class="before__star">★</span>
    <span class="before__ribbon-title">Rehearsal Dinner</span>
    <span class="before__star">★</span>
  </div>

  <div class="before__dates">
    <svg class="chevrons" viewBox="0 0 34 24" aria-hidden="true"><path d="M2 2 L12 12 L2 22 M16 2 L26 12 L16 22" fill="none" stroke="var(--teal)" stroke-width="5"/></svg>
    <div class="date-box">
      <div class="date-box__top">FRIDAY</div>
      <div class="date-box__bottom">5.30 PM</div>
    </div>
    <div class="date-box">
      <div class="date-box__top">MAY</div>
      <div class="date-box__bottom">22, 2015</div>
    </div>
  </div>

  <address class="before__venue">
    <div class="before__venue-name">★ Larkvale Grub Yard ★</div>
    <div class="before__venue-street">617 Tessler Avenue @ Marlow San Francisco, CA</div>
  </address>

  <div class="before__details">
    <div class="detail-box detail-box--dress"><span>DRESS<br>CASUAL</span></div>
    <div class="detail-box detail-box--food">
      <div class="detail-box__script">Food Beer &amp; Wine</div>
      <div class="detail-box__note">Held in a private enclosed space in the food truck park</div>
    </div>
  </div>
  <div class="before__band-bottom"></div>
</section>

<section class="card card--after" aria-label="After party invitation">
  <div class="after__frame"></div>
  <div class="after__label">AFTER</div>
  <div class="after__tuxedo" role="img" aria-label="Black tuxedo with bow tie and red pocket square illustration"></div>
  <h1 class="after__names">Derek &amp; Simon</h1>
  <div class="after__title">AFTER PARTY</div>
  <div class="after__rule after__rule--one"></div>
  <div class="after__date">SATURDAY, MAY 23, 2015</div>
  <div class="after__rule after__rule--two"></div>
  <address class="after__where">
    7:30 PM, @Corvell Harbor Sailing Club<br>42 Pennick Lane, San Francisco, CA
  </address>
  <div class="after__rule after__rule--three"></div>
  <p class="after__note">Black-tie (optional), Dancing, Snacks, dessert and cocktails<br>panoramic views of the San Francisco Bay &amp; Golden Gate Bridge</p>
</section>

</body>
</html>
```